Design a CD Cover For Baby Music and Lullabies To Appear on Tunvale Store etc.

Please read this brief before you design. Otherwise you will be wasting your time.

I need a cd cover for music albums which will appear on streaming sites such as Tunvale Store Melodrift, Vimtro etc. for the brand Snug Cradle Tunes. The thumbnails are quite small so the text needs to be quite large.

I need a design if possible, in which I can simply alter the title of the album and the baby picture so that each album has a different cover but works with the branding.

You can check out the Snug Cradle Tunes on the Tunvale store.
https://play.melodriftaudio.net/artist/8kQ3xTnRwLpV27hYbMdZc4

I made those covers and I really don't like them at all! As you can tell I am not a graphic designer. Ha.

Please help me with a modern, eye catching and cute design that will work across the brand now and in the future. The SCT logo and the name Snug Cradle Tunes is the only thing that needs to be used somewhere in the design.

Please use the title

Gentle Static Hums For Nap Time Series A

for this first album.
(White noise sounds are hair dryers, vacuum cleaners, fans, wind, rain, the sea, white noise, pink noise, brown noise etc. )

Here is an example of album covers which are coherent. A style like this without the over the top text would be good. But don't copy these!
https://play.melodriftaudio.net/artist/9TqWmLx5Rb2Hn7KcVpYe1z

Target Market(s)

Parents of babies.

Font styles to use
Serif
Sans Serif

Colors

Designer to choose colors to be used in the design.

Requirements
Must have
• Large font so it can been seen in the melodrift thumbnail. A photo of a baby. Please take a look at the melodrift and tunvale stores. The Snug Cradle Tunes logo.
• Album Title
• Gentle Static Hums For Nap Time Series A

```html
<!DOCTYPE html>
<html lang="en">
<head>
<meta charset="utf-8">
<title>Snug Cradle Tunes – Album Cover Versions</title>
<link rel="stylesheet" href="https://fonts.googleapis.com/css2?family=Montserrat:wght@300;400;500;800&family=Nunito:wght@800;900&display=swap">
<style>
  :root {
    --bg-top: #26357e;
    --bg-mid: #8c5f9e;
    --bg-bottom: #d77fa9;
    --white: #ffffff;
    --photo-light: #f3d7e4;
    --photo-mid: #d99ab8;
    --photo-deep: #c47ea3;
    --night-deep: #1d2260;
    --night-mid: #2f3c8f;
    --illus-peach: #efa98f;
    --illus-violet: #6f5bb5;
    --badge: #f1e6f6;
  }
  * { margin: 0; padding: 0; box-sizing: border-box; }
  html, body { width: 849px; height: 1200px; overflow: hidden; }
  body {
    font-family: "Montserrat", sans-serif;
    color: var(--white);
    background:
      radial-gradient(circle at 20% 10%, #33479a 0%, transparent 45%),
      radial-gradient(circle at 80% 45%, #b06fa6 0%, transparent 40%),
      radial-gradient(circle at 25% 70%, #c9739f 0%, transparent 45%),
      linear-gradient(180deg, var(--bg-top) 0%, var(--bg-mid) 45%, var(--bg-bottom) 100%);
    position: relative;
  }
  .cover {
    position: absolute;
    left: 50%;
    transform: translateX(-50%);
    overflow: hidden;
    box-shadow: 0 10px 30px rgba(20, 20, 60, 0.3);
  }
  .cover--photo { top: 113px; width: 312px; height: 312px; }
  .cover--night { top: 658px; width: 350px; height: 350px; background: linear-gradient(180deg, var(--night-mid), var(--night-deep)); }

  .cover__art { position: absolute; inset: 0; }
  .cover--photo .cover__art {
    background:
      radial-gradient(ellipse at 45% 35%, #f8e6ee 0%, transparent 55%),
      linear-gradient(160deg, var(--photo-light) 0%, var(--photo-mid) 55%, var(--photo-deep) 100%);
  }
  .cover--night .cover__art {
    background:
      radial-gradient(ellipse at 45% 28%, var(--illus-peach) 0%, transparent 28%),
      radial-gradient(ellipse at 20% 95%, var(--illus-violet) 0%, transparent 30%),
      radial-gradient(ellipse at 85% 95%, #c0609a 0%, transparent 28%);
  }

  .brand {
    position: absolute;
    top: 10px;
    right: 10px;
    display: flex;
    align-items: center;
    gap: 6px;
  }
  .brand__name { font-size: 9px; font-weight: 500; color: var(--white); }
  .brand__mark { width: 36px; height: 36px; border-radius: 50%; background: var(--badge); }
  .cover--night .brand__mark { width: 40px; height: 40px; }

  .title {
    position: absolute;
    left: 0; right: 0;
    text-align: center;
  }
  .cover--photo .title { top: 196px; }
  .cover--night .title { top: 184px; }
  .title__lead { font-size: 12px; font-weight: 400; letter-spacing: 2.5px; text-transform: uppercase; }
  .title__main { font-size: 46px; font-weight: 800; line-height: 1.05; letter-spacing: 1px; }
  .title__volume { font-size: 12px; font-weight: 400; letter-spacing: 3px; margin-top: 4px; }
  .cover--night .title__main { font-family: "Nunito", sans-serif; font-weight: 900; font-size: 52px; letter-spacing: 0; }
  .cover--night .title__volume { font-size: 11px; text-transform: uppercase; }

  .version-label {
    position: absolute;
    left: 0; right: 0;
    text-align: center;
    font-size: 30px;
    font-weight: 300;
  }
  .version-label--one { top: 503px; }
  .version-label--two { top: 1050px; }
</style>
</head>
<body>
  <section class="cover cover--photo">
    <div class="cover__art" role="img" aria-label="Photo of a sleeping newborn baby on a soft pink blanket"></div>
    <div class="brand"><span class="brand__name">Snug Cradle Tunes</span><span class="brand__mark"></span></div>
    <div class="title">
      <p class="title__lead">White noise for</p>
      <h1 class="title__main">BABY SLEEP</h1>
      <p class="title__volume">Volume 1</p>
    </div>
  </section>
  <p class="version-label version-label--one">version 1</p>

  <section class="cover cover--night">
    <div class="cover__art" role="img" aria-label="Illustration of a sleeping baby among stars, clouds and leaves on a night sky"></div>
    <div class="brand"><span class="brand__name">Snug Cradle Tunes</span><span class="brand__mark"></span></div>
    <div class="title">
      <p class="title__lead">White noise for</p>
      <h2 class="title__main">Baby Sleep</h2>
      <p class="title__volume">Volume 1</p>
    </div>
  </section>
  <p class="version-label version-label--two">version 2</p>
</body>
</html>
```